RMT Blazin' Riverdale, American Quarter Horse Stallion Stud Services

Advertisement for stud service. I'd like to showcase how stunningly beautiful this horse is with the full-body pic and how sweet, gentle, and quiet he is with the other pic. I want two-sided cards with photos on both sides. Headshot (cropped) on front with info on management, contact #s, etc. Full-body, datepair.example-type pic on back with some information on his pedigree. I'd like something striking enough that even if people don't want the service, they keep the card.

Target Market(s)

Horse owners, horse breeders, horse trainers, equestrians

Industry/Entity Type

Contact Information for Business Card

Horse's name: RMT Blazin' Riverdale
Owner: Norma Tillet
Manager: Cory Lindqvist
Phone: 208-555-0147
Pedigree information: Sire - Oaks Mon Pierrot, Dam - Bright Maned Lucerita
Sire's parents: Riverdale Dox 42 (sire) and Cedars Lovely Belle (dam)
Dam's parents: Shez Lucerita (sire) and Bright Maned Waltz (dam)

Font styles to use
Sans Serif

Requirements
Must have
• Rich, distinctive look. Should be a stand-out card; one that people keep even if they're not interested in the service.
Nice to have
• Pedigree information displayed in a family-tree arrangement. The horse is black, so I am picturing cards that are mostly black, probably with white or off-white (cream-colored) lettering. In fact, the horse has what's known as the cream-color gene, so maybe cream-colored would be better.

```html
<!DOCTYPE html>
<html lang="en">
<head>
<meta charset="utf-8">
<title>RMT Blazin' Riverdale – Business Card</title>
<link rel="stylesheet" href="https://fonts.googleapis.com/css2?family=Source+Sans+3:wght@400;500&display=swap">
<style>
  :root {
    --backdrop: #6d6e71;
    --card-cream: #fcfaf1;
    --ink: #1f1c1a;
    --label-tan: #c49a83;
    --photo-dark: #2e2520;
    --photo-mid: #6a5a50;
    --photo-light: #d9d2c4;
  }
  * { margin: 0; padding: 0; box-sizing: border-box; }
  html, body {
    width: 1194px;
    height: 1200px;
    overflow: hidden;
    background: var(--backdrop);
    font-family: "Source Sans 3", sans-serif;
  }
  .stage {
    width: 1194px;
    height: 1200px;
    display: flex;
    align-items: center;
    justify-content: center;
  }
  .business-card {
    position: relative;
    width: 1000px;
    height: 571px;
    background: var(--card-cream);
    overflow: hidden;
    box-shadow: 0 10px 30px rgba(0, 0, 0, 0.25);
  }
  .horse-photo {
    position: absolute;
    top: 0;
    right: 0;
    width: 500px;
    height: 100%;
    background:
      radial-gradient(ellipse 45% 55% at 35% 40%, rgba(46, 37, 32, 0.85), rgba(46, 37, 32, 0) 70%),
      radial-gradient(ellipse 60% 45% at 80% 30%, var(--photo-dark), rgba(46, 37, 32, 0) 75%),
      linear-gradient(180deg, var(--photo-mid) 0%, var(--photo-light) 100%);
    -webkit-mask-image: linear-gradient(90deg, transparent 0%, rgba(0,0,0,0.55) 30%, #000 60%);
    mask-image: linear-gradient(90deg, transparent 0%, rgba(0,0,0,0.55) 30%, #000 60%);
  }
  .card-info {
    position: absolute;
    left: 48px;
    top: 98px;
    color: var(--ink);
  }
  .horse-name {
    font-size: 36px;
    font-weight: 400;
    letter-spacing: 0.5px;
    margin-bottom: 46px;
  }
  .contact-row { margin-bottom: 30px; }
  .contact-label {
    display: block;
    font-size: 19px;
    color: var(--label-tan);
    line-height: 1;
    margin-bottom: 6px;
  }
  .contact-value {
    display: block;
    font-size: 33px;
    line-height: 1.1;
  }
</style>
</head>
<body>
  <main class="stage">
    <section class="business-card">
      <div class="horse-photo" role="img" aria-label="Photo of the black stallion's head in a bridle, fading into the cream card"></div>
      <div class="card-info">
        <h1 class="horse-name">RMT Blazin' Riverdale</h1>
        <div class="contact-row">
          <span class="contact-label">owner</span>
          <span class="contact-value">Norma Tillet</span>
        </div>
        <div class="contact-row">
          <span class="contact-label">manager</span>
          <span class="contact-value">Cory Lindqvist</span>
        </div>
        <div class="contact-row">
          <span class="contact-label">phone</span>
          <span class="contact-value">208.555.0147</span>
        </div>
      </div>
    </section>
  </main>
</body>
</html>
```